Kelmora Legal Business Card

I require a corporate business card for a new legal services business.

I do not have a logo, nor do I want one.

I require a clean, neat a professional card for a law firm.

Details:

Business Name: Kelmora Legal
Name: Debra Lindqvist
Title: Corporate Services Manager
Location: Office 14 (Top Floor), Toravel Business Centre, Quinlan Grove Street, Alotau CBD, Milne Bay Province.
Postal Address: PO Box 593, Alotau, 211, Milne Bay Province, Papua New Guinea.
Contact: T: +675 6418250, F: +675 6413362, M: +675 72915867, E: dlindqvist@kelmoraexample.com.pg.

I look forward to your design submissions.

Industry/Entity Type

Legal

```html
<!DOCTYPE html>
<html lang="en">
<head>
<meta charset="utf-8">
<title>Kelmora Legal – Business Card</title>
<link rel="stylesheet" href="https://fonts.googleapis.com/css2?family=Bellefair&display=swap">
<style>
  :root {
    --paper: #ffffff;
    --ink: #111111;
    --card-font: "Bellefair", serif;
  }
  html, body {
    margin: 0;
    padding: 0;
    width: 1200px;
    height: 702px;
    overflow: hidden;
    background: var(--paper);
  }
  .card {
    position: relative;
    width: 1200px;
    height: 702px;
    overflow: hidden;
    background: var(--paper);
    color: var(--ink);
    font-family: var(--card-font);
  }
  .firm-name {
    position: absolute;
    right: 661px;
    top: 69px;
    margin: 0;
    font-weight: 400;
    font-size: 146px;
    line-height: 133px;
    text-align: right;
    letter-spacing: -0.5px;
    white-space: nowrap;
  }
  .firm-name span { display: block; }
  .address {
    position: absolute;
    right: 661px;
    margin: 0;
    font-style: normal;
    font-size: 31px;
    line-height: 31.5px;
    text-align: right;
    white-space: nowrap;
  }
  .address span { display: block; }
  .address--street { top: 374px; }
  .address--postal { top: 531px; }
  .person {
    position: absolute;
    left: 670px;
    top: 152px;
  }
  .person-name {
    margin: 0;
    font-weight: 400;
    font-size: 60px;
    line-height: 66px;
    letter-spacing: 1.5px;
    white-space: nowrap;
  }
  .person-title {
    margin: 0;
    font-size: 36px;
    line-height: 40px;
    letter-spacing: 1px;
    white-space: nowrap;
  }
  .email {
    position: absolute;
    left: 670px;
    top: 325px;
    margin: 0;
    font-size: 34px;
    line-height: 40px;
    letter-spacing: 0.5px;
    white-space: nowrap;
  }
  .phones {
    position: absolute;
    left: 670px;
    top: 422px;
    margin: 0;
    padding: 0;
    list-style: none;
    font-size: 48px;
    line-height: 54px;
    white-space: nowrap;
  }
</style>
</head>
<body>
  <main class="card">
    <h1 class="firm-name"><span>Kelmora</span><span>Legal</span></h1>

    <address class="address address--street">
      <span>Office 14 (Top Floor)</span>
      <span>Toravel Business Centre</span>
      <span>Quinlan Grove Street</span>
      <span>Alotau CBD, Milne Bay Province</span>
    </address>

    <address class="address address--postal">
      <span>PO Box 593</span>
      <span>Alotau, 211</span>
      <span>Milne Bay Province</span>
      <span>Papua New Guinea</span>
    </address>

    <section class="person">
      <h2 class="person-name">Debra Lindqvist</h2>
      <p class="person-title">Corporate Services Manager</p>
    </section>

    <p class="email">dlindqvist@kelmoraexample.com.pg</p>

    <ul class="phones">
      <li>T: +675.641.8250</li>
      <li>F: +675.641.3362</li>
      <li>M: +675.729.15867</li>
    </ul>
  </main>
</body>
</html>
```